Silent Thicket

Creation of a cover for the book "Fourré muet" (French text): a polar about a person dying (from unidentified gunshot) during hauting in a forest. The cover intends to suggest the mood of the haunting in the wood and the intervention of an police captain.

The image of the forest is provided: hunter in front of a pond.
We ask the graphist to find a photo of a Police lieutenant. SEE AN EXAMPLE ATTACHED (it is important to show a "French look" lieutenant.

The cover doesn't need to be an exact photo, it can be any image (drawing for example) derived from these two pictures.

Book Publisher

Requirements
Must have
• Size of the book: 14 x 20.5 cm (vertical)
Title: Silent thicket
Author: Mireille Tassard
Publisher: Editions Korvane (at the bottom of the page)

```html
<!DOCTYPE html>
<html lang="fr">
<head>
<meta charset="utf-8">
<title>Silent Thicket — Mireille Tassard</title>
<link rel="stylesheet" href="https://fonts.googleapis.com/css2?family=Russo+One&family=Montserrat:wght@300;400&display=swap">
<style>
  :root {
    --page-bg: #e7e7e7;
    --band-red: #a3262a;
    --band-red-light: #b23a3c;
    --ink-white: #f4f1ee;
    --night: #1b1b1c;
    --dusk-gold: #d8c98a;
    --water-grey: #77715f;
    --fog: #cbb894;
    --forest-dark: #2a2522;
    --publisher-grey: #6c6c6c;
  }
  * { box-sizing: border-box; margin: 0; padding: 0; }
  html, body {
    width: 1000px;
    height: 1200px;
    overflow: hidden;
    background: var(--page-bg);
  }
  .cover {
    position: absolute;
    left: 130px;
    top: 58px;
    width: 740px;
    height: 1084px;
    overflow: hidden;
    background: var(--night);
    box-shadow: 0 18px 40px rgba(0, 0, 0, 0.25);
  }
  .scene-pond {
    position: absolute;
    left: 0; top: 0;
    width: 100%;
    height: 520px;
    background:
      radial-gradient(ellipse 60% 50% at 50% 45%, transparent 40%, rgba(20, 20, 20, 0.75) 100%),
      radial-gradient(ellipse 30% 9% at 62% 14%, rgba(230, 215, 150, 0.9), transparent 75%),
      radial-gradient(ellipse 22% 22% at 66% 40%, rgba(215, 200, 130, 0.75), transparent 75%),
      linear-gradient(180deg, #4a4a44 0%, #2e2e2b 10%, #2b2b28 16%, var(--water-grey) 26%, #5e5a4d 55%, #3b3934 80%, var(--night) 100%);
  }
  .scene-forest {
    position: absolute;
    left: 0; top: 620px;
    width: 100%;
    height: 464px;
    background:
      radial-gradient(ellipse 55% 50% at 50% 45%, transparent 35%, rgba(18, 16, 15, 0.8) 100%),
      radial-gradient(ellipse 38% 36% at 55% 18%, rgba(228, 210, 165, 0.9), transparent 75%),
      linear-gradient(180deg, var(--fog) 0%, #7a6a56 30%, var(--forest-dark) 68%, #151312 100%);
  }
  .blood-band {
    position: absolute;
    left: 0; top: 0;
    width: 100%;
    height: 100%;
  }
  .title-block {
    position: absolute;
    left: 0;
    top: 497px;
    width: 100%;
    text-align: center;
    color: var(--ink-white);
  }
  .title {
    font-family: "Russo One", "Impact", sans-serif;
    font-weight: 400;
    font-size: 62px;
    line-height: 1;
    letter-spacing: 1px;
    text-transform: uppercase;
  }
  .author {
    margin-top: 10px;
    padding-left: 60px;
    font-family: "Montserrat", "Helvetica", sans-serif;
    font-weight: 400;
    font-size: 30px;
    letter-spacing: 3px;
  }
  .publisher {
    position: absolute;
    left: 0;
    bottom: 58px;
    width: 100%;
    text-align: center;
    font-family: "Montserrat", "Helvetica", sans-serif;
    font-weight: 300;
    font-size: 16px;
    letter-spacing: 17px;
    text-transform: uppercase;
    color: var(--publisher-grey);
  }
</style>
</head>
<body>
  <main class="cover">
    <div class="scene-pond" role="img" aria-label="Hunter silhouetted at dusk on the edge of a pond among bare branches, holding game"></div>
    <div class="scene-forest" role="img" aria-label="Police lieutenant in a long coat walking away down a misty forest path"></div>

    <svg class="blood-band" viewBox="0 0 740 1084" aria-hidden="true">
      <defs>
        <linearGradient id="bandShade" x1="0" y1="0" x2="1" y2="0">
          <stop offset="0" stop-color="#9c2326"/>
          <stop offset="0.6" stop-color="#a82d30"/>
          <stop offset="1" stop-color="#b23a3c"/>
        </linearGradient>
      </defs>
      <g fill="url(#bandShade)">
        <path d="
          M0 486 C8 474 16 496 28 478 C40 458 52 484 66 466 C80 448 92 446 108 456
          C120 464 134 430 152 440 C168 448 182 424 200 432 C214 438 222 414 238 420
          L250 400 L258 418 C276 410 290 398 310 404 C330 410 342 388 364 394
          C384 400 396 380 418 386 C436 392 450 366 472 374 C490 380 502 360 526 366
          C546 372 556 348 580 354 C600 360 614 340 636 346 C652 350 664 330 682 338
          C700 346 708 326 722 332 C730 336 736 326 740 328
          L740 648 C730 644 724 662 712 652 C700 642 694 628 684 640
          L676 612 L670 646 C656 660 648 640 634 654 C620 668 604 652 590 664
          C574 676 560 660 544 674 C528 688 512 672 496 684 C480 696 466 682 448 694
          C432 704 418 690 402 702 C386 714 370 700 352 712 C338 722 322 708 306 720
          C290 732 274 718 258 730 C242 742 226 728 210 740 C194 752 178 738 162 748
          L150 776 L146 750 C130 760 116 746 98 756 C82 766 66 752 50 762
          C36 770 22 758 10 768 C6 772 2 766 0 768 Z"/>
        <circle cx="38" cy="450" r="6"/>
        <circle cx="92" cy="430" r="4"/>
        <circle cx="142" cy="414" r="5"/>
        <circle cx="176" cy="402" r="3"/>
        <circle cx="228" cy="390" r="4"/>
        <circle cx="300" cy="380" r="3"/>
        <circle cx="356" cy="368" r="5"/>
        <circle cx="412" cy="362" r="3"/>
        <circle cx="486" cy="344" r="4"/>
        <circle cx="540" cy="338" r="6"/>
        <circle cx="602" cy="322" r="3"/>
        <circle cx="660" cy="312" r="5"/>
        <circle cx="712" cy="300" r="3"/>
        <circle cx="264" cy="330" r="3"/>
        <circle cx="590" cy="290" r="4"/>
        <circle cx="70" cy="790" r="5"/>
        <circle cx="120" cy="782" r="3"/>
        <circle cx="210" cy="768" r="4"/>
        <circle cx="276" cy="758" r="6"/>
        <circle cx="330" cy="744" r="3"/>
        <circle cx="384" cy="734" r="4"/>
        <circle cx="438" cy="724" r="5"/>
        <circle cx="470" cy="748" r="3"/>
        <circle cx="520" cy="708" r="4"/>
        <circle cx="566" cy="700" r="3"/>
        <circle cx="618" cy="688" r="5"/>
        <circle cx="660" cy="680" r="3"/>
        <circle cx="30" cy="820" r="4"/>
        <circle cx="250" cy="800" r="3"/>
      </g>
    </svg>

    <div class="title-block">
      <h1 class="title">Silent Thicket</h1>
      <p class="author">Mireille Tassard</p>
    </div>

    <p class="publisher">Editions Korvane</p>
  </main>
</body>
</html>
```